Yard sign

I want it to look similar to this one,

change name to DRAVEK and submit new ideas

Also would like to improvise a bit. let's not make exactly the same thing

would like to change to: Connecticut #1 Company

also change phone to 203-555-0147
and website to
dravekllc.com

this is yard sign. size is 24' Width and 32' Height

Target Market(s)

Roof

Industry/Entity Type

Roofing

Requirements
Must have
• similar colors or add something new

```html
<!DOCTYPE html>
<html lang="en">
<head>
<meta charset="utf-8">
<title>Dravek Roofing Yard Sign</title>
<link rel="stylesheet" href="https://fonts.googleapis.com/css2?family=Cormorant+Garamond:wght@500;600&family=Baloo+2:wght@800&family=Montserrat:wght@500;700&display=swap">
<style>
  :root {
    --paper: #ffffff;
    --ink-grey: #6b6f72;
    --brand-orange: #f5a11c;
    --slate: #273139;
    --slate-band: #3b454c;
    --number-grey: #c8cbcd;
    --icon-grey: #5d666c;
  }
  * { margin: 0; padding: 0; box-sizing: border-box; }
  html, body { width: 835px; height: 1200px; overflow: hidden; background: var(--paper); }
  .sign {
    position: relative;
    width: 835px;
    height: 1200px;
    overflow: hidden;
    background: var(--paper);
  }
  .sign-shapes { position: absolute; inset: 0; }
  .tagline-top {
    position: absolute;
    top: 118px;
    width: 100%;
    text-align: center;
    font-family: "Cormorant Garamond", serif;
    font-weight: 600;
    font-size: 62px;
    line-height: 76px;
    letter-spacing: 3px;
    font-variant-numeric: lining-nums;
    color: var(--ink-grey);
    text-transform: uppercase;
  }
  .brand-name {
    position: absolute;
    top: 282px;
    width: 100%;
    text-align: center;
    font-family: "Baloo 2", sans-serif;
    font-weight: 800;
    font-size: 176px;
    line-height: 170px;
    letter-spacing: 12px;
    color: var(--brand-orange);
  }
  .slogan {
    position: absolute;
    top: 492px;
    width: 100%;
    text-align: center;
    font-family: "Cormorant Garamond", serif;
    font-weight: 600;
    font-size: 50px;
    letter-spacing: 3px;
    color: var(--ink-grey);
    text-transform: uppercase;
  }
  .phone-icon {
    position: absolute;
    left: 395px;
    top: 810px;
    width: 46px;
    height: 46px;
  }
  .phone-band {
    position: absolute;
    left: 0;
    top: 876px;
    width: 100%;
    height: 92px;
    background: var(--slate-band);
  }
  .phone-number {
    position: absolute;
    top: 876px;
    width: 100%;
    text-align: center;
    font-family: "Montserrat", sans-serif;
    font-weight: 700;
    font-size: 74px;
    line-height: 92px;
    letter-spacing: 3px;
    color: var(--number-grey);
  }
  .website {
    position: absolute;
    top: 1028px;
    width: 100%;
    text-align: center;
    font-family: "Montserrat", sans-serif;
    font-weight: 500;
    font-size: 30px;
    letter-spacing: 6px;
    color: var(--brand-orange);
    text-transform: uppercase;
  }
</style>
</head>
<body>
  <main class="sign">
    <svg class="sign-shapes" width="835" height="1200" viewBox="0 0 835 1200" aria-hidden="true">
      <polygon class="roof-trim" points="0,728 417,598 835,728 835,766 417,636 0,766" fill="var(--brand-orange)"/>
      <polygon class="roof-base" points="0,782 417,652 835,782 835,1200 0,1200" fill="var(--slate)"/>
    </svg>

    <p class="tagline-top">Connecticut #1<br>Company</p>
    <h1 class="brand-name">DRAVEK</h1>
    <p class="slogan">Quality you can trust</p>

    <svg class="phone-icon" viewBox="0 0 48 48" aria-hidden="true">
      <path d="M4 16c0-6 9-9 20-9s20 3 20 9v4h-10v-5c-3-1-6-1.5-10-1.5s-7 .5-10 1.5v5H4z" fill="var(--icon-grey)"/>
      <path d="M12 22h24l6 12v8H6v-8z" fill="var(--icon-grey)"/>
      <circle cx="24" cy="33" r="5" fill="var(--slate)"/>
    </svg>

    <div class="phone-band"></div>
    <p class="phone-number">203-555-0147</p>
    <p class="website">www.dravekllc.com</p>
  </main>
</body>
</html>
```